poster for escape room advertising the themes of our rooms, bold, samples attached

we need poster advertising our 4 escape room themes. The Crimson Ledger, (doctor, test tube) Midnight Carnival, (retro items, time machine) The Velvet Parlour (serial killer, clown, doll, knives) and , moonspire (island, ship, compass). Primarily black and white with red and yellow.
samples attached. Comic book or bold graphic theme. More information can be found on our website quillgatepuzzles.com.

• impact, anything bold, almost comic book

fbee3c
ec1f27
ffffff
000000
5c5c5c
9d9d9d
cbcbcb
e8e8e8
cfcfcf

• title of each room, The Crimson Ledger, Midnight Carnival, The Velvet Parlour, Moonspire. Graphic representing each theme.
• short description of rooms

```html
<!DOCTYPE html>
<html lang="en">
<head>
<meta charset="utf-8">
<title>Quillgate Puzzles – Can You Escape?</title>
<link href="https://fonts.googleapis.com/css2?family=Anton&family=Creepster&family=Roboto+Condensed:wght@300;400;700&family=Roboto:wght@400;500&display=swap" rel="stylesheet">
<style>
  :root {
    --yellow: #fbee3c;
    --red: #ec1f27;
    --white: #ffffff;
    --black: #000000;
    --grey-dark: #5c5c5c;
    --grey-mid: #9d9d9d;
    --grey-light: #cbcbcb;
    --paper: #e8e8e8;
    --olive: #5b5a3e;
    --teal: #3fb7b0;
  }
  * { margin: 0; padding: 0; box-sizing: border-box; }
  html, body { width: 1200px; height: 1200px; overflow: hidden; }
  body { background: var(--paper); position: relative; font-family: "Roboto Condensed", Arial, sans-serif; }

  .poster { position: absolute; left: 212px; top: 0; width: 776px; height: 1200px; background: var(--black); overflow: hidden; }

  .backdrop { position: absolute; left: 0; top: 0; width: 776px; height: 560px;
    background: radial-gradient(ellipse at 78% 40%, #2a2a2a 0%, #151515 35%, transparent 70%),
                linear-gradient(180deg, #1b1b1b 0%, #101010 60%, #000 100%); }

  .band { position: absolute; top: 74px; height: 50px; background: var(--yellow); }
  .band--left { left: 0; width: 238px; }
  .band--right { left: 547px; width: 229px; }

  .brand-block { position: absolute; left: 240px; top: 0; width: 304px; height: 267px; background: var(--black);
    display: flex; flex-direction: column; align-items: center; justify-content: center; gap: 14px; }
  .brand-mark { width: 22px; height: 22px; background: var(--yellow); }
  .brand-name { font-family: "Anton", Impact, sans-serif; font-size: 40px; color: var(--yellow); letter-spacing: 1px; line-height: 1; text-align: center; }

  .headline { position: absolute; left: 0; width: 776px; top: 268px; text-align: center;
    font-family: "Anton", Impact, sans-serif; font-size: 82px; line-height: 1; color: var(--red); letter-spacing: 1px; }
  .subhead { position: absolute; left: 0; width: 776px; top: 356px; text-align: center;
    font-weight: 700; font-size: 31px; color: var(--yellow); }
  .capacity { position: absolute; left: 0; width: 776px; top: 396px; text-align: center;
    font-weight: 300; font-size: 26px; color: var(--yellow); }
  .intro { position: absolute; left: 0; width: 776px; top: 440px; text-align: center;
    font-size: 19px; line-height: 24px; color: var(--white); }

  .doors-art { position: absolute; left: 206px; top: 500px; width: 320px; height: 600px;
    background: radial-gradient(ellipse at 50% 45%, #d8d8d8 0%, #6d6d6d 18%, #1a1a1a 45%, #000 72%); }

  .room { position: absolute; width: 218px; }
  .room--ledger { left: 59px; top: 542px; width: 164px; }
  .room--parlour { left: 528px; top: 548px; }
  .room--carnival { left: 59px; top: 816px; width: 164px; }
  .room--moonspire { left: 528px; top: 814px; }

  .room__the { font-weight: 300; font-size: 25px; line-height: 1; color: var(--yellow); }
  .room--parlour .room__the { color: var(--white); }
  .room__title { font-family: "Anton", Impact, sans-serif; line-height: 1; }
  .room--ledger .room__title { color: var(--yellow); }
  .title-lg { font-size: 56px; }
  .title-md { font-size: 44px; }
  .room--parlour .room__title { color: var(--red); }
  .title-script { font-family: "Creepster", "Anton", cursive; font-size: 50px; line-height: 1; color: var(--red); }
  .title-grey { color: var(--grey-mid); font-size: 44px; }
  .title-olive { color: var(--olive); font-size: 48px; }
  .title-teal { color: var(--teal); font-size: 58px; display: inline-block; transform: scaleY(1.75); transform-origin: top left; height: 104px; }

  .room__text { margin-top: 8px; font-family: "Roboto", Arial, sans-serif; font-size: 9.4px; line-height: 11px;
    color: var(--yellow); text-align: justify; }
  .room__cta { position: absolute; left: 0; font-size: 20px; color: var(--yellow); }
  .room--ledger .room__cta, .room--parlour .room__cta { top: 216px; }
  .room--carnival .room__cta, .room--moonspire .room__cta { top: 200px; }

  .footer { position: absolute; left: 0; top: 1100px; width: 776px; height: 100px; background: var(--yellow); }
  .footer__lead { position: absolute; left: 53px; top: 14px; font-weight: 700; font-size: 23px; color: var(--black); }
  .footer__rules { position: absolute; left: 332px; top: 12px; width: 444px; height: 22px; }
  .contact { position: absolute; top: 50px; display: flex; align-items: center; gap: 8px; color: var(--black); }
  .contact--address { left: 53px; font-family: "Roboto", Arial, sans-serif; font-size: 14px; line-height: 17px; }
  .contact--phone { left: 271px; font-weight: 700; font-size: 29px; }
  .contact--email { left: 528px; top: 56px; font-family: "Roboto", Arial, sans-serif; font-size: 15px; }
</style>
</head>
<body>
<main class="poster">
  <div class="backdrop" role="img" aria-label="Dark photograph of an abandoned corridor with a barred gate"></div>

  <div class="band band--left"></div>
  <div class="band band--right"></div>

  <div class="brand-block">
    <span class="brand-mark"></span>
    <span class="brand-name">QUILLGATE PUZZLES</span>
  </div>

  <h1 class="headline">CAN YOU ESCAPE?</h1>
  <p class="subhead">PRIVATE ESCAPE GAME EXPERIENCE</p>
  <p class="capacity">( UP TO 10 PEOPLE)</p>
  <p class="intro">WE ARE A FENWICK AND HARLOW SPRINGS TEXAS BASED ESCAPE GAME EXPERIENCE<br>WITH THREE ROOMS CURRENTLY AVAILABLE AND A FOURTH ROOM ON THE WAY!</p>

  <div class="doors-art" role="img" aria-label="Illustration of two glowing open doorways with a microbe, a dripping red hand, an ornate golden key and a sailing ship"></div>

  <section class="room room--ledger">
    <div class="room__the">THE</div>
    <div class="room__title title-md">CRIMSON</div>
    <div class="room__title title-lg">LEDGER</div>
    <p class="room__text">is a great for groups looking for a more challenging experience, especially for those interested in a medical or science theme. The puzzles in this escape game are more 'task-oriented' and will have everyone in your group saying "OOH, that's so cool!".</p>
    <div class="room__cta">BOOK NOW</div>
  </section>

  <section class="room room--parlour">
    <div class="room__the">THE</div>
    <div class="room__title title-md">VELVET</div>
    <div class="title-script">PARLOUR</div>
    <p class="room__text">offers a heart-pounding and thrilling experience. Our goal is to provide an fun-filled hour that will keep groups tense and excited up until the final seconds.</p>
    <div class="room__cta">BOOK NOW</div>
  </section>

  <section class="room room--carnival">
    <div class="room__title title-grey">MIDNIGHT</div>
    <div class="room__title title-olive">CARNIVAL</div>
    <p class="room__text">escape room is great for groups who enjoy a fun, nostalgic experience. While still challenging, the focus of this escape game is having a great time with friends or family.</p>
    <div class="room__cta">BOOK NOW</div>
  </section>

  <section class="room room--moonspire">
    <div class="room__title title-teal">MOONSPIRE</div>
    <p class="room__text">is a great for groups looking for a more challenging experience, especially for those interested in a medical or science theme. The puzzles in this escape game are more 'task-oriented' and will have everyone in your group saying "OOH, that's so cool!".</p>
    <div class="room__cta">BOOK NOW</div>
  </section>

  <footer class="footer">
    <p class="footer__lead">Contact Today For Services</p>
    <svg class="footer__rules" viewBox="0 0 444 22" aria-hidden="true">
      <rect x="0" y="2" width="444" height="3" fill="#000"/>
      <rect x="0" y="8" width="444" height="3" fill="#000"/>
      <rect x="0" y="14" width="444" height="3" fill="#000"/>
    </svg>
    <div class="contact contact--address">
      <svg width="30" height="40" viewBox="0 0 30 40" aria-hidden="true">
        <path d="M15 1C7.3 1 1.5 6.8 1.5 14.3 1.5 24 15 39 15 39s13.5-15 13.5-24.7C28.5 6.8 22.7 1 15 1z" fill="#000"/>
        <circle cx="15" cy="14" r="6" fill="var(--yellow)"/>
      </svg>
      <span>4180 Larkspur Avenue<br>Suite 212, Fenwick TX</span>
    </div>
    <div class="contact contact--phone">
      <svg width="24" height="34" viewBox="0 0 24 34" aria-hidden="true">
        <path d="M6 1l5 7-3 4c1.5 5 4 9 8 13l4-2 4 7-5 3C10 32 2 20 1 6z" fill="#000"/>
      </svg>
      <span>(555) 804-3162</span>
    </div>
    <div class="contact contact--email">
      <svg width="38" height="26" viewBox="0 0 38 26" aria-hidden="true">
        <rect x="1.5" y="1.5" width="35" height="23" fill="none" stroke="#000" stroke-width="3"/>
        <path d="M2 2l17 13L36 2M2 24l12-11M36 24L24 13" fill="none" stroke="#000" stroke-width="2.5"/>
      </svg>
      <span>info@quillgatepuzzles.com</span>
    </div>
  </footer>
</main>
</body>
</html>
```